Breeze Pod Sensor App Splash Screen

We are not really looking for a logo, but it's the closest category I could pick. We need a graphic for our SPLASH SCREEN which shows for about 3-5 seconds while the app is loading during startup.

Our app focuses on Air Quality Monitoring and our product is called the "Breeze Pod Sensor". In this graphic we would like to portray how using our product will allow users to easily use the devices they have purchased and improve their life by gaining insights about air pollutants in their local environment.

This screen can have some text e.g. "Care About Your Air", or "Measure, Share, Breath" are a couple of copy ideas, but others are welcome.

For reference, our "old" webpage for Breeze Pod Sensor is at http://breezepodsensor.com and our shop website is at https://shop.tallowgear.com/product-category/breeze-pod-sensor//.

Target Market(s)

Our primary markets are Citizen Science and Education

Logo Text

We're flexible... see Project Description (want more art than text)

Font styles to use
Sans Serif

Requirements
Must have
• The source image’s minimum dimensions should be 2208x2208 px, and its artwork should be centered within the square, knowing that each generated image will be center cropped into landscape and portrait images. The splash screen’s artwork should roughly fit within a center square (1200x1200 px). Photoshop template is available here: http://code.pemberkit.com/resources/splash.psd
• See technical requirements / guidance at http://pemberkit.com/docs/v1/cli/icon-splashscreen.html.
Nice to have
• The egg theme would be nice to maintain but can easily be deviated from if a clearer message can be conveyed without it.
Should not have
• Any text content should be limited to something the user can digest in 3 seconds or less.

```html
<!DOCTYPE html>
<html lang="en">
<head>
<meta charset="utf-8">
<title>Breeze Pod Sensor — Splash</title>
<link rel="stylesheet" href="https://fonts.googleapis.com/css2?family=Open+Sans:wght@700&display=swap">
<style>
  :root {
    --sky: #03aeef;
    --white: #ffffff;
  }
  html, body {
    margin: 0;
    padding: 0;
    overflow: hidden;
  }
  .splash {
    position: relative;
    width: 1200px;
    height: 1200px;
    background: var(--sky);
    color: var(--white);
    font-family: "Open Sans", Arial, sans-serif;
    font-weight: 700;
    overflow: hidden;
  }
  .brand {
    position: absolute;
    left: 0;
    right: 0;
    top: 508px;
    display: flex;
    align-items: center;
    justify-content: center;
    gap: 28px;
  }
  .brand-mark {
    width: 46px;
    height: 46px;
    border-radius: 50%;
    background: var(--white);
    flex: none;
  }
  .brand-name {
    margin: 0;
    font-size: 76px;
    line-height: 1;
    letter-spacing: -0.5px;
    font-weight: 700;
  }
  .loader {
    position: absolute;
    left: 371px;
    top: 987px;
    width: 458px;
    height: 26px;
  }
  .tagline {
    position: absolute;
    left: 0;
    right: 0;
    top: 1044px;
    margin: 0;
    text-align: center;
    font-size: 28px;
    letter-spacing: 1.5px;
    text-transform: uppercase;
  }
</style>
</head>
<body>
  <main class="splash">
    <div class="brand">
      <span class="brand-mark" aria-hidden="true"></span>
      <h1 class="brand-name">Breeze Pod Sensor</h1>
    </div>

    <svg class="loader" viewBox="0 0 458 26" role="img" aria-label="Loading progress">
      <rect x="1.5" y="1.5" width="455" height="23" rx="11.5" fill="none" stroke="var(--white)" stroke-width="3"/>
      <path d="M13 1.5 H318 V24.5 H13 A11.5 11.5 0 0 1 13 1.5 Z" fill="var(--white)"/>
    </svg>

    <p class="tagline">Care about your air</p>
  </main>
</body>
</html>
```